Marrowfen Vodka label redesign

This label was originally screen-printed. I would like it redesigned to fit a new rectangular paper label that will cover the screen-printed label of a different bottle than what was previously earmarked for a different product. I can easily resize the elements from the original label to fit the new size, but I would like to see some creative options for the new size. Show me what you've got!
Here are some guidelines:
New label must contain the butterfly and text "Marrowfen" in its existing font (that's our logo) the color is optional. It must also contain the barcode and all other text elements but font, style, size and color can change:
The Government warning text cannot be smaller. Style and font cannot change, but the justification can change.
The filigree does not have to stay.
The previous label was broken up into 3 panels. The new label will be one solid label encircling the bottle. The label size will be 10.5" x 5.5" (266.7 mm x 139.7 mm) AI template attached.

Target Market(s)

Women age 35 and up with disposable income

Font styles to use
Other font styles liked:
• Mostra Nuova

Colors

Designer to choose colors to be used in the design.

Requirements
Must have
• Class
Nice to have
• ArtDeco elements
Should not have
• Sharp edges

```html
<!DOCTYPE html>
<html lang="en">
<head>
<meta charset="utf-8">
<title>Marrowfen Spirits – Vodka Label</title>
<link rel="stylesheet" href="https://fonts.googleapis.com/css2?family=Poiret+One&family=Josefin+Sans:wght@400;600&display=swap">
<style>
  :root {
    --ink: #2d2c93;
    --ink-mid: #8d8cc8;
    --ink-light: #c9c9e6;
    --ink-wash: #e6e6f4;
    --paper: #ffffff;
  }
  html, body {
    margin: 0;
    padding: 0;
    width: 1200px;
    height: 561px;
    overflow: hidden;
    background: var(--paper);
  }
  .canvas {
    position: relative;
    width: 1200px;
    height: 561px;
  }
  .label {
    position: absolute;
    left: 96px;
    top: 15px;
    width: 1007px;
    height: 530px;
    color: var(--ink);
    font-family: "Josefin Sans", sans-serif;
  }
  .label__frame {
    position: absolute;
    inset: 0;
  }

  .corner-ornament {
    position: absolute;
    width: 104px;
    height: 104px;
    box-sizing: border-box;
    border: 1.5px solid var(--ink);
    background: linear-gradient(135deg, var(--ink-light) 0%, var(--ink-wash) 100%);
  }
  .corner-ornament--tl { left: 0; top: 0; border-radius: 8px 8px 52px 8px; }
  .corner-ornament--tr { right: 0; top: 0; border-radius: 8px 8px 8px 52px; }
  .corner-ornament--bl { left: 0; bottom: 0; border-radius: 8px 52px 8px 8px; }
  .corner-ornament--br { right: 0; bottom: 0; border-radius: 52px 8px 8px 8px; }

  .wreath {
    position: absolute;
    left: 232px;
    top: 92px;
    width: 544px;
    height: 336px;
  }

  .panel {
    position: absolute;
    left: 377px;
    top: 82px;
    width: 256px;
    height: 316px;
    box-sizing: border-box;
    border: 1.5px solid var(--ink);
    border-radius: 6px;
    background: var(--paper);
    text-align: center;
  }
  .brand-mark {
    width: 84px;
    height: 84px;
    margin: 22px auto 0;
    border-radius: 50%;
    background: var(--ink);
  }
  .brand-name {
    margin: 22px 0 0;
    font-family: "Poiret One", sans-serif;
    font-weight: 400;
    font-size: 34px;
    line-height: 34px;
    color: var(--ink);
  }
  .tagline {
    margin: 6px 0 0;
    font-size: 17px;
    line-height: 18px;
  }
  .product {
    margin: 6px 0 0;
    font-size: 64px;
    line-height: 56px;
    letter-spacing: 1px;
  }
  .strength {
    margin: 2px 0 0;
    font-size: 12.5px;
    line-height: 14px;
    letter-spacing: 0.2px;
  }
  .origin {
    position: absolute;
    left: 0;
    right: 0;
    top: 440px;
    margin: 0;
    text-align: center;
    font-size: 12.5px;
    letter-spacing: 0.4px;
  }
  .side-heading {
    position: absolute;
    top: 136px;
    margin: 0;
    font-size: 12px;
    font-weight: 600;
    letter-spacing: 0.3px;
  }
  .side-heading--details { left: 96px; }
  .side-heading--code { left: 826px; }
</style>
</head>
<body>
<div class="canvas">
  <section class="label">
    <svg class="label__frame" width="1007" height="530" viewBox="0 0 1007 530" aria-hidden="true">
      <g fill="none" stroke="var(--ink)" stroke-width="1.5" stroke-linecap="round">
        <line x1="104" y1="17" x2="440" y2="17"/>
        <line x1="567" y1="17" x2="903" y2="17"/>
        <line x1="104" y1="21" x2="440" y2="21" stroke-width="0.8"/>
        <line x1="567" y1="21" x2="903" y2="21" stroke-width="0.8"/>
        <path d="M440 19 q32 -14 63 0 q32 -14 64 0"/>
        <line x1="104" y1="509" x2="440" y2="509"/>
        <line x1="567" y1="509" x2="903" y2="509"/>
        <line x1="104" y1="513" x2="440" y2="513" stroke-width="0.8"/>
        <line x1="567" y1="513" x2="903" y2="513" stroke-width="0.8"/>
        <path d="M440 511 q32 14 63 0 q32 14 64 0"/>
        <line x1="18" y1="104" x2="18" y2="426"/>
        <line x1="22" y1="104" x2="22" y2="426" stroke-width="0.8"/>
        <line x1="989" y1="104" x2="989" y2="426"/>
        <line x1="985" y1="104" x2="985" y2="426" stroke-width="0.8"/>
      </g>
    </svg>

    <div class="corner-ornament corner-ornament--tl" role="img" aria-label="Filigree corner ornament with rosette"></div>
    <div class="corner-ornament corner-ornament--tr" role="img" aria-label="Filigree corner ornament with rosette"></div>
    <div class="corner-ornament corner-ornament--bl" role="img" aria-label="Filigree corner ornament with rosette"></div>
    <div class="corner-ornament corner-ornament--br" role="img" aria-label="Filigree corner ornament with rosette"></div>

    <p class="side-heading side-heading--details">OTHER DETAILS</p>
    <p class="side-heading side-heading--code">BARCODE</p>

    <svg class="wreath" width="544" height="336" viewBox="0 0 544 336" role="img" aria-label="Botanical wreath of leafy branches and berries framing the centre panel">
      <defs>
        <linearGradient id="wreath-tone" x1="0" y1="0" x2="0" y2="1">
          <stop offset="0" stop-color="var(--ink-wash)"/>
          <stop offset="1" stop-color="var(--ink-light)"/>
        </linearGradient>
      </defs>
      <g fill="url(#wreath-tone)" stroke="var(--ink-mid)" stroke-width="1.2">
        <path d="M150 10 C90 40 20 120 4 180 C30 250 90 300 150 326 Z"/>
        <path d="M394 10 C454 40 524 120 540 180 C514 250 454 300 394 326 Z"/>
        <path d="M150 300 C200 336 344 336 394 300 L394 326 C344 340 200 340 150 326 Z"/>
      </g>
    </svg>

    <div class="panel">
      <div class="brand-mark" aria-hidden="true"></div>
      <h1 class="brand-name">Marrowfen<br>Spirits</h1>
      <p class="tagline">Small -Batch Premium</p>
      <p class="product">VODKA</p>
      <p class="strength">ALCOHOL 40% BY VALUE 80 PROOF</p>
    </div>

    <p class="origin">HOLLIN VALLEY, OREGON, US</p>
  </section>
</div>
</body>
</html>
```